Need help refining Tallbergsgillet

Hi We need help with the refining of overall design and details of our homepage design Tallbergsgillet. See attached files.

Attached files:
homepage.psd - file you can use to work from.
homepage.png – quick notes on thoughts of the design
logo.psd (smart object) – The logo should be in gold.
social media elements.png - what type of data that needs design in the feed

What we need:
Something is missing with the overall design as well as detailed design for our social media feed. We don’t know what and hope you can solve this for us.

The homepage:
Our main page include a selfloading blogfeed combined with Vendraly- and Instagramfeed.

Fonts:
So far I´ve used Roboto regular, and Georgia, but feel free to use other fonts if you find better suited

Among others, we need a better detailed design that works better with the overall design.

Se attached sample image (social_mediafeed.png) what types of data we get from Vendraly in our feed. Feel free to redesign the elements of this data.

Headerlinks:
Even though we only have one page, there should be place for links to other pages as well which will load below the header.

Social media follow: Place for social media follow links/icons/buttons in style with rest of the design. Maybe at top grey border? We use Glimtora and Vendraly in style with rest of the design.

Colors:
The logo should be in gold, and use of "goldish" colors troughout the page.
Also blue elements troughout the page

Logo in gold/goldish color
Blue elements # 13416c (or similar color that works well in the design)

Target Market(s)

Wellness, fitness, spa and food, Exclusive

Number of Pages Required

1 page

Font styles to use
Serif
Sans Serif
Script
Other font styles liked:
• Roboto, Georgia

Requirements
Must have
• Better overall design that feel harmonic.
• Better design of blog and social media feeds (se all attached images)
• Nice clean design, easy on the eye
• Colors on theme: Gold + blue

```html
<!DOCTYPE html>
<html lang="en">
<head>
<meta charset="utf-8">
<title>Tallbergsgillet — Home</title>
<link rel="stylesheet" href="https://fonts.googleapis.com/css2?family=Montserrat:wght@400;500;600;700&family=Lora:ital,wght@0,400;0,600;1,400&display=swap">
<style>
:root{
  --gold:#eab42a;
  --gold-dark:#c99a1c;
  --blue:#13416c;
  --ink:#2b2b2b;
  --muted:#8a8a8a;
  --line:#e4e4e4;
  --page:#f4f4f4;
  --white:#ffffff;
  --dark:#232323;
  --sans:'Montserrat', Arial, sans-serif;
  --serif:'Lora', Georgia, serif;
}
*{box-sizing:border-box;margin:0;padding:0}
html,body{width:1200px;height:2951px;overflow:hidden}
body{position:relative;background:var(--page);font-family:var(--sans);color:var(--ink)}
.abs{position:absolute}
.ph{display:block}

/* top bar */
.topbar{left:0;top:0;width:1200px;height:28px;background:#f1f1f1;border-bottom:1px solid #e6e6e6}
.topbar .social{left:325px;top:9px;display:flex;gap:10px}
.dot-ico{width:9px;height:9px;border-radius:50%;background:#9a9a9a}
.dot-ico.gold{background:var(--gold)}
.topbar .account{left:770px;top:9px;font-size:7px;letter-spacing:1px;color:#999;display:flex;gap:5px;align-items:center}

/* header */
.header{left:0;top:28px;width:1200px;height:96px;background:var(--white)}
.nav{top:37px;width:265px;height:28px;border-top:1px solid #cfcfcf;border-bottom:1px solid #cfcfcf;display:flex;justify-content:space-between;align-items:center;padding:0 16px;font-size:8px;letter-spacing:1px;text-transform:uppercase;font-weight:500}
.nav.left{left:250px}
.nav.right{left:685px}
.nav a{color:var(--ink);text-decoration:none}
.nav a.active{color:var(--gold)}
.brand{left:520px;top:18px;width:160px;text-align:center}
.brand .mark{width:22px;height:22px;border:1.5px solid var(--gold);border-radius:50%;margin:0 auto 5px}
.brand .name{font-family:var(--serif);font-size:13px;color:var(--gold);letter-spacing:.5px;border-top:1px solid var(--gold);border-bottom:1px solid var(--gold);padding:3px 0}

/* hero */
.hero{left:0;top:124px;width:1200px;height:271px;overflow:hidden}
.hero .side{top:0;height:271px;width:208px;background:linear-gradient(180deg,#dfe4ef,#c9cbdd 55%,#b9c2d8)}
.hero .side::after{content:"";position:absolute;inset:0;background:rgba(255,255,255,.55)}
.hero .side.l{left:0}.hero .side.r{left:991px}
.hero .slide{left:208px;top:0;width:783px;height:271px;background:linear-gradient(180deg,#8c8d8f 0%,#b69b7d 45%,#6b6460 75%,#3f3a36 100%)}
.hero .arrow{top:102px;width:24px;height:78px;border:1px solid #555;background:rgba(255,255,255,.6);font-size:8px;font-weight:600;color:#333;display:flex;flex-direction:column;align-items:center;justify-content:center;line-height:11px}
.hero .arrow.prev{left:94px}.hero .arrow.next{left:1084px}
.hero .caption{left:208px;top:90px;width:783px;text-align:center;color:#fff}
.tag{display:inline-block;background:var(--gold);color:#fff;font-size:7px;font-weight:600;letter-spacing:1px;text-transform:uppercase;padding:3px 10px}
.hero h1{font-family:var(--sans);font-weight:500;font-size:17px;margin-top:10px}
.hero .byline{font-family:var(--serif);font-style:italic;font-size:10px;margin-top:7px}
.btn-ghost{display:inline-block;border:1px solid #fff;color:#fff;font-size:7px;letter-spacing:1px;padding:6px 14px;margin-top:16px}
.hero .dots{left:580px;top:242px;display:flex;gap:5px}
.hero .dots span{width:5px;height:5px;border-radius:50%;background:#fff}
.hero .dots span.on{border:1px solid #fff;background:transparent;width:7px;height:7px;margin-top:-1px}

/* section titles */
.section-title{left:0;width:1200px;text-align:center;font-size:20px;font-weight:600;color:#222}

/* paper fold */
.paper{background:var(--white);box-shadow:0 1px 2px rgba(0,0,0,.06)}
.paper::after{content:"";position:absolute;right:0;bottom:0;width:0;height:0;border-style:solid;border-width:0 0 14px 14px;border-color:transparent transparent var(--page) #e2e2e2}

/* offers */
.offers{left:250px;top:472px;width:700px;height:334px}
.offer{top:18px;width:208px;height:269px}
.offer .pic{position:absolute;inset:0}
.offer .box{position:absolute;left:14px;top:132px;width:183px;height:125px;background:rgba(255,255,255,.94);text-align:center;padding-top:20px}
.offer .box .tag{position:absolute;left:50%;top:-6px;transform:translateX(-50%)}
.offer .pct{font-family:var(--serif);font-size:17px;color:var(--blue)}
.offer .pct span{font-size:14px}
.offer .desc{font-size:9.5px;line-height:13px;margin-top:4px;color:#333}
.btn-line{display:inline-block;border:1px solid var(--blue);color:var(--blue);font-size:7px;letter-spacing:1px;padding:5px 14px;margin-top:9px}
.offers .arrows{left:16px;top:302px;display:flex;gap:12px}

.divider{left:0;top:840px;width:1200px;height:1px;background:#e1e1e1}

/* posts */
.post{background:var(--white)}
.post .pic{position:absolute}
.post .tag{position:absolute}
.post h3{position:absolute;left:0;width:100%;text-align:center;font-weight:500;font-size:11px;line-height:15px;color:#222}
.post .date{position:absolute;left:0;width:100%;text-align:center;font-family:var(--serif);font-size:8px;color:#444}
.post .excerpt{position:absolute;text-align:center;font-family:var(--serif);font-size:8px;line-height:13px;color:#7a7a7a}
.post .meta{position:absolute;display:flex;justify-content:space-between;font-family:var(--serif);font-size:7.5px;color:#777}
.post .meta span{display:flex;align-items:center;gap:4px}
.post .more{position:absolute;left:0;width:100%;text-align:center;font-family:var(--serif);font-size:8.5px;color:var(--gold);text-decoration:underline}
.ribbon{left:250px;top:934px;width:16px;height:80px;background:var(--blue);color:#fff;font-family:var(--serif);font-size:7px;writing-mode:vertical-rl;transform:rotate(180deg);display:flex;align-items:center;justify-content:center}

/* sidebar */
.widget{left:704px;width:246px}
.widget .head{height:35px;background:var(--blue);color:#fff;font-size:9.5px;font-weight:500;letter-spacing:.5px;display:flex;align-items:center;justify-content:center}
.widget .head.gold-edge{border-bottom:3px solid var(--gold)}
.about-seal{left:70px;top:54px;width:106px;height:106px;border-radius:50%;background:radial-gradient(circle at 45% 40%,#8a6a52,#4d3626);box-shadow:0 0 0 4px #f0ece8}
.about-seal span{position:absolute;left:0;top:46px;width:100%;text-align:center;font-family:var(--serif);font-size:9px;color:#e9d6b8}
.widget .about-text{position:absolute;left:22px;top:176px;width:202px;text-align:center;font-family:var(--serif);font-size:7.5px;line-height:11.5px;color:#777}
.widget .about-btn{position:absolute;left:76px;top:258px}
.cats{list-style:none;padding:10px 20px 0}
.cats li{font-family:var(--serif);font-size:8px;color:#555;height:33px;display:flex;align-items:center;border-bottom:1px solid #eee}
.feed{left:20px;top:54px;width:208px;height:299px;border:1px solid #dcdcdc;background:#fff}
.feed .cover{position:absolute;left:0;top:0;width:206px;height:90px;background:linear-gradient(180deg,#4a3e36,#7a644f)}
.feed .page-name{position:absolute;left:40px;top:8px;font-size:9px;font-weight:600;color:#fff}
.feed .page-sub{position:absolute;left:40px;top:21px;font-size:6.5px;color:#eee}
.feed .avatar{position:absolute;left:8px;top:8px;width:26px;height:26px;background:var(--blue);border:1.5px solid #fff}
.feed .like{position:absolute;left:8px;top:64px;background:#f3f3f3;color:#333;font-size:6.5px;padding:3px 6px;border:1px solid #ccc}
.feed .share{position:absolute;left:160px;top:64px;background:#f3f3f3;color:#333;font-size:6.5px;padding:3px 6px;border:1px solid #ccc}
.feed .friends{position:absolute;left:8px;top:96px;font-size:6.5px;color:#555}
.feed .faces{position:absolute;left:8px;top:110px;display:flex;gap:2px}
.feed .faces span{width:16px;height:16px;background:#b7aaa0}
.feed .rule{position:absolute;left:0;top:135px;width:206px;height:1px;background:#ddd}
.feed .post-head{position:absolute;left:8px;top:144px;display:flex;gap:6px;align-items:center}
.feed .post-head i{width:18px;height:18px;background:var(--blue);display:block}
.feed .post-head b{font-size:7px;color:#365899;font-weight:600;display:block}
.feed .post-head em{font-size:6px;color:#999;font-style:normal}
.feed .post-body{position:absolute;left:8px;top:170px;font-size:7px;line-height:10px;color:#333;width:185px}
.feed .post-img{position:absolute;left:8px;top:202px;width:185px;height:86px;background:linear-gradient(180deg,#5f86b3,#9ab6cf 60%,#8a8f8a)}
.feed .scroll{position:absolute;right:2px;top:96px;width:4px;height:60px;background:#ccc;border-radius:2px}
.chirp-dot{position:absolute;left:115px;top:56px;width:14px;height:14px;border-radius:50%;background:var(--blue)}
.chirp-handle{position:absolute;left:0;top:80px;width:100%;text-align:center;font-family:var(--serif);font-size:7.5px;color:var(--gold)}
.chirp-text{position:absolute;left:24px;top:100px;width:198px;text-align:center;font-family:var(--serif);font-size:7.5px;line-height:11.5px;color:#777}
.chirp-dots{position:absolute;left:96px;top:179px;display:flex;gap:5px}
.chirp-dots span{width:8px;height:4px;background:#ccc;border-radius:2px}
.chirp-dots span.on{background:var(--gold);width:14px}

/* pagination */
.pager{left:0;top:2276px;width:1200px;display:flex;justify-content:center;align-items:center;font-size:7px;letter-spacing:1px;color:#555}
.pager .edge{width:70px;height:20px;background:#fff;border:1px solid #e6e6e6;display:flex;align-items:center;justify-content:center}
.pager .nums{display:flex;gap:8px;margin:0 22px 0 30px}
.pager .nums span{width:20px;height:20px;background:#fff;border:1px solid #e6e6e6;display:flex;align-items:center;justify-content:center}
.pager .nums span.on{background:var(--gold);color:#fff;border-color:var(--gold)}

/* glimtora strip */
.strip-bg{left:0;top:2331px;width:1200px;height:462px;background:var(--white)}
.strip-sub{left:0;top:2395px;width:1200px;text-align:center;font-family:var(--serif);font-size:8px;color:var(--gold)}
.strip{left:0;top:2433px;width:1200px;height:148px;display:flex}
.strip .ph{flex:1;height:148px;position:relative}
.strip .overlay{position:absolute;inset:0;background:rgba(0,0,0,.35)}
.strip .overlay i{position:absolute;left:63px;top:62px;width:24px;height:24px;border-radius:50%;background:rgba(255,255,255,.35)}

/* footer */
.foot-brand{left:520px;top:2620px;width:160px;text-align:center}
.foot-brand .mark{width:18px;height:18px;border:1.5px solid var(--gold);border-radius:50%;margin:0 auto 4px}
.foot-brand .name{font-family:var(--serif);font-size:10px;color:var(--gold);border-top:1px solid var(--gold);border-bottom:1px solid var(--gold);padding:2px 0}
.foot-text{left:440px;top:2676px;width:320px;text-align:center;font-family:var(--serif);font-size:8.5px;line-height:13px;color:#777}
.sub-title{left:0;top:2747px;width:1200px;text-align:center;font-size:10px;color:#333}
.dark{left:0;top:2793px;width:1200px;height:158px;background:var(--dark)}
.sub-form{left:464px;top:2782px;width:270px;height:22px;display:flex;background:#fff;border:1px solid #ddd;z-index:2}
.sub-form .field{flex:1;font-family:var(--serif);font-size:7.5px;color:#999;padding:6px 8px}
.sub-form .go{width:22px;background:var(--gold);display:flex;align-items:center;justify-content:center}
.foot-social{left:0;top:2843px;width:1200px;display:flex;justify-content:center;gap:8px}
.foot-social span{width:24px;height:24px;border-radius:50%;border:1px solid #777;display:flex;align-items:center;justify-content:center}
.foot-social span i{width:6px;height:6px;border-radius:50%;background:#bbb}
.foot-social span.on{border-color:var(--gold)}
.foot-social span.on i{background:var(--gold)}
.copy{left:0;top:2902px;width:1200px;text-align:center;font-family:var(--serif);font-size:8.5px;color:#ddd}
</style>
</head>
<body>

<!-- top bar -->
<div class="abs topbar">
  <div class="abs social" aria-label="Social links">
    <span class="dot-ico"></span><span class="dot-ico gold"></span><span class="dot-ico"></span><span class="dot-ico"></span><span class="dot-ico"></span><span class="dot-ico"></span>
  </div>
  <div class="abs account">
    <svg width="8" height="8" viewBox="0 0 8 8"><circle cx="4" cy="2.5" r="1.8" fill="#aaa"/><path d="M0.5 8c0-2 1.6-3 3.5-3s3.5 1 3.5 3z" fill="#aaa"/></svg>
    LOGIN / SIGN UP
  </div>
</div>

<!-- header -->
<header class="abs header">
  <nav class="abs nav left"><a href="#">Home</a><a href="#" class="active">About Us</a><a href="#">Inspiration</a></nav>
  <div class="abs brand"><div class="mark"></div><div class="name">Tallbergsgillet</div></div>
  <nav class="abs nav right"><a href="#">Member Offers</a><a href="#">Om</a><a href="#">Contact Us</a></nav>
</header>

<!-- hero slider -->
<section class="abs hero">
  <div class="abs side l" role="img" aria-label="Previous slide photo: overwater villas at dusk"></div>
  <div class="abs slide" role="img" aria-label="Slide photo: photographer on a rocky shore at sunset"></div>
  <div class="abs side r" role="img" aria-label="Next slide photo: jetty over calm water"></div>
  <div class="abs arrow prev">P<br>R<br>E<br>V</div>
  <div class="abs arrow next">N<br>E<br>X<br>T</div>
  <div class="abs caption">
    <span class="tag">Life Style</span>
    <h1>How to Spend a Week in the Maldives</h1>
    <p class="byline">June 26<sup>th</sup>, 2016 &nbsp;–&nbsp; By Elin Varg</p>
    <span class="btn-ghost">READ MORE</span>
  </div>
  <div class="abs dots"><span></span><span></span><span class="on"></span><span></span><span></span></div>
</section>

<!-- member offers -->
<h2 class="abs section-title" style="top:428px">Member Offers</h2>
<section class="abs offers paper">
  <article class="abs offer" style="left:17px">
    <div class="pic" role="img" aria-label="Photo: mountain valley landscape" style="background:linear-gradient(180deg,#b7c0cc,#8a7a6a 45%,#3e3d4a)"></div>
    <div class="box"><span class="tag">Travel</span><div class="pct">70% <span>Off</span></div><div class="desc">International Flights<br>Bookings</div><span class="btn-line">LEARN MORE</span></div>
  </article>
  <article class="abs offer" style="left:246px">
    <div class="pic" role="img" aria-label="Photo: hotel room with curtains" style="background:linear-gradient(90deg,#e3dcd8,#a48aa8 45%,#6d4f7a)"></div>
    <div class="box"><span class="tag">Hotel</span><div class="pct">60% <span>Off</span></div><div class="desc">Offering Lowest Hotel<br>Booking Prices</div><span class="btn-line">LEARN MORE</span></div>
  </article>
  <article class="abs offer" style="left:474px">
    <div class="pic" role="img" aria-label="Photo: fashion detail with boots" style="background:linear-gradient(160deg,#c9b49c,#7c6450 50%,#2c2623)"></div>
    <div class="box"><span class="tag">Fashion</span><div class="pct">50% <span>Off</span></div><div class="desc">Widest Range Of Designer<br>Cloths</div><span class="btn-line">LEARN MORE</span></div>
  </article>
  <div class="abs arrows">
    <svg width="10" height="8" viewBox="0 0 10 8"><path d="M9 4H1M4 1L1 4l3 3" stroke="#999" fill="none"/></svg>
    <svg width="10" height="8" viewBox="0 0 10 8"><path d="M1 4h8M6 1l3 3-3 3" stroke="#eab42a" fill="none"/></svg>
  </div>
</section>

<div class="abs divider"></div>

<!-- blog -->
<h2 class="abs section-title" style="top:870px">Our Latest Blog</h2>

<article class="abs post paper" style="left:250px;top:934px;width:432px;height:423px">
  <div class="pic" role="img" aria-label="Photo: traveller on a desert road among red rocks" style="left:17px;top:0;width:402px;height:179px;background:linear-gradient(180deg,#cbd6de,#b98a6a 45%,#8a6a58 70%,#6f6b66)"></div>
  <span class="tag" style="left:191px;top:174px">Travel</span>
  <h3 style="top:202px">The standard Lorem Ipsum passage</h3>
  <p class="excerpt" style="left:28px;top:224px;width:376px">There are many variations of passages of Lorem Ipsum available, but the majority have suffered alteration in some form, by injected humour, or randomised words which don't look even slightly believable. If you are going to use a passage of Lorem Ipsum, you need to be sure there isn't anything embarrassing hidden in the middle of text. All the Lorem Ipsum generators on the Internet tend to repeat predefined chunks as necessary, making this the...</p>
  <div class="meta" style="left:18px;top:333px;width:396px">
    <span><svg width="7" height="8" viewBox="0 0 7 8"><circle cx="3.5" cy="2" r="1.8" fill="#888"/><path d="M0 8c0-2 1.5-3 3.5-3S7 6 7 8z" fill="#888"/></svg>Lorem</span>
    <span><svg width="8" height="7" viewBox="0 0 8 7"><path d="M1 1h6v4H3L1 6.5z" stroke="#888" fill="none"/></svg>30 Comment</span>
    <span><svg width="8" height="7" viewBox="0 0 8 7"><path d="M4 6.5L1 3.5A1.6 1.6 0 014 1.5 1.6 1.6 0 017 3.5z" stroke="#888" fill="none"/></svg>25 Likes</span>
    <span><svg width="8" height="8" viewBox="0 0 8 8"><circle cx="6.5" cy="1.5" r="1.2" fill="#888"/><circle cx="1.5" cy="4" r="1.2" fill="#888"/><circle cx="6.5" cy="6.5" r="1.2" fill="#888"/><path d="M6.5 1.5L1.5 4l5 2.5" stroke="#888" fill="none" stroke-width=".7"/></svg>Share</span>
  </div>
  <a class="more" style="top:374px">Continue Reading</a>
</article>
<div class="abs ribbon">June 26<sup>th</sup>, 2016</div>

<!-- small posts -->
<article class="abs post paper" style="left:250px;top:1379px;width:208px;height:415px">
  <div class="pic" role="img" aria-label="Photo: winding road through autumn forest" style="left:17px;top:18px;width:174px;height:118px;background:linear-gradient(135deg,#6e7a3a,#c97b2c 50%,#3f4a2c)"></div>
  <span class="tag" style="left:73px;top:131px">Travel</span>
  <p class="date" style="top:169px">24 Jun, 2016</p>
  <h3 style="top:184px">The standard Lorem<br>Ipsum passage</h3>
  <p class="excerpt" style="left:16px;top:222px;width:176px">There are many variations of passages of Lorem Ipsum available, but the majority have suffered alteration in some form, by injected humour, or randomised words which don't look even stratum...</p>
  <div class="meta" style="left:16px;top:324px;width:176px"><span>● Lorem</span><span>○ 30 Comment</span><span>◦ Share</span></div>
  <a class="more" style="top:368px">Continue Reading</a>
</article>
<article class="abs post paper" style="left:478px;top:1379px;width:204px;height:415px">
  <div class="pic" role="img" aria-label="Photo: woman in a hat among green leaves" style="left:17px;top:18px;width:170px;height:118px;background:linear-gradient(135deg,#4e5e3a,#2d2a24 55%,#7b6d55)"></div>
  <span class="tag" style="left:69px;top:131px">Lifestyle</span>
  <p class="date" style="top:169px">18 Jun, 2016</p>
  <h3 style="top:184px">The standard Lorem<br>Ipsum passage</h3>
  <p class="excerpt" style="left:14px;top:222px;width:176px">There are many variations of passages of Lorem Ipsum available, but the majority have suffered alteration in some form, by injected humour, or randomised words which don't look even stratum...</p>
  <div class="meta" style="left:14px;top:324px;width:176px"><span>● Lorem</span><span>○ 30 Comment</span><span>◦ Share</span></div>
  <a class="more" style="top:368px">Continue Reading</a>
</article>
<article class="abs post paper" style="left:250px;top:1821px;width:208px;height:416px">
  <div class="pic" role="img" aria-label="Photo: person sitting on a bench in autumn" style="left:17px;top:18px;width:174px;height:118px;background:linear-gradient(135deg,#6a4a3a,#a68a72 50%,#4a3a32)"></div>
  <span class="tag" style="left:73px;top:131px">Fashion</span>
  <p class="date" style="top:169px">02 Jul, 2016</p>
  <h3 style="top:184px">The standard Lorem<br>Ipsum passage</h3>
  <p class="excerpt" style="left:16px;top:222px;width:176px">There are many variations of passages of Lorem Ipsum available, but the majority have suffered alteration in some form, by injected humour, or randomised words which don't look even stratum...</p>
  <div class="meta" style="left:16px;top:324px;width:176px"><span>● Lorem</span><span>○ 30 Comment</span><span>◦ Share</span></div>
  <a class="more" style="top:368px">Continue Reading</a>
</article>
<article class="abs post paper" style="left:478px;top:1821px;width:204px;height:416px">
  <div class="pic" role="img" aria-label="Photo: woman in a hat outdoors" style="left:17px;top:18px;width:170px;height:118px;background:linear-gradient(135deg,#5e6a4a,#c9b89a 50%,#3e4030)"></div>
  <span class="tag" style="left:69px;top:131px">Celebrity</span>
  <p class="date" style="top:169px">02 Aug, 2016</p>
  <h3 style="top:184px">The standard Lorem<br>Ipsum passage</h3>
  <p class="excerpt" style="left:14px;top:222px;width:176px">There are many variations of passages of Lorem Ipsum available, but the majority have suffered alteration in some form, by injected humour, or randomised words which don't look even stratum...</p>
  <div class="meta" style="left:14px;top:324px;width:176px"><span>● Lorem</span><span>○ 30 Comment</span><span>◦ Share</span></div>
  <a class="more" style="top:368px">Continue Reading</a>
</article>

<!-- sidebar -->
<aside class="abs widget paper" style="top:915px;height:305px">
  <div class="head gold-edge">About Me</div>
  <div class="abs about-seal" role="img" aria-label="Brand seal on leather"><span>Tallbergsgillet</span></div>
  <p class="about-text">Ipsum, by injected humour, or randomised words which don't look even slightly believable. If you are going to use a passage of Lorem Ipsum, you need to be sure there isn't anything embarrassing hidden in the middle of text.</p>
  <span class="about-btn btn-line">READ MORE</span>
</aside>

<aside class="abs widget paper" style="top:1255px;height:289px">
  <div class="head gold-edge">Categories</div>
  <ul class="cats"><li>Fashion</li><li>Travel</li><li>Lifestyle</li><li>Music &amp; Video</li><li>Food Recipies</li><li>Photography</li><li>Celibrity</li></ul>
</aside>

<aside class="abs widget paper" style="top:1574px;height:373px">
  <div class="head gold-edge">Vendraly</div>
  <div class="abs feed">
    <div class="cover" role="img" aria-label="Page cover photo"></div>
    <div class="avatar"></div>
    <div class="page-name">Tallbergsgillet</div>
    <div class="page-sub">12,847 likes</div>
    <span class="like">Like Page</span>
    <span class="share">Share</span>
    <div class="friends">Be the first of your friends to like this</div>
    <div class="faces"><span></span><span></span><span></span><span></span><span></span><span></span><span></span></div>
    <div class="scroll"></div>
    <div class="rule"></div>
    <div class="post-head"><i></i><div><b>Tallbergsgillet</b><em>8 November at 12:44</em></div></div>
    <p class="post-body">Ett nytt liv väntar dig här. Bli en del av gillet idag. #tallbergsgillet</p>
    <div class="post-img" role="img" aria-label="Post photo: person with raised arms by the sea"></div>
  </div>
</aside>

<aside class="abs widget paper" style="top:1993px;height:244px">
  <div class="head gold-edge">Latest Chirps</div>
  <span class="chirp-dot"></span>
  <p class="chirp-handle">@tallbergsgillet</p>
  <p class="chirp-text">Sed ut perspiciatis unde omnis iste natus error sit voluptatem accusantium doloremque laudantium, totam rem aperiam. <span style="color:var(--gold)">#gillet</span></p>
  <div class="chirp-dots"><span></span><span></span><span class="on"></span><span></span><span></span></div>
</aside>

<!-- pagination -->
<nav class="abs pager">
  <span class="edge">PREV</span>
  <div class="nums"><span class="on">1</span><span>2</span><span>3</span><span>4</span><span>5</span></div>
  <span class="edge">NEXT</span>
</nav>

<!-- glimtora -->
<div class="abs strip-bg"></div>
<h2 class="abs section-title" style="top:2367px">Glimtora</h2>
<p class="abs strip-sub">Follow @tallbergsgillet</p>
<div class="abs strip">
  <div class="ph" role="img" aria-label="Photo: man sitting outdoors" style="background:linear-gradient(135deg,#3a4a3a,#7a6a4a)"></div>
  <div class="ph" role="img" aria-label="Photo: legs on a wooden bench" style="background:linear-gradient(135deg,#5a6a7a,#2a2f38)"></div>
  <div class="ph" role="img" aria-label="Photo: person on a dark road" style="background:linear-gradient(135deg,#5a5a58,#2e2e2c)"><div class="overlay"><i></i></div></div>
  <div class="ph" role="img" aria-label="Photo: woman in a red hat by a lake" style="background:linear-gradient(180deg,#c9d3dc,#9aa6a8 50%,#6a7068)"></div>
  <div class="ph" role="img" aria-label="Photo: person in an autumn park" style="background:linear-gradient(135deg,#8a5a3a,#c9a06a 50%,#4a3a2a)"></div>
  <div class="ph" role="img" aria-label="Photo: sneakers on pavement" style="background:linear-gradient(135deg,#8a9098,#4a4e56)"></div>
  <div class="ph" role="img" aria-label="Photo: photographer with a camera" style="background:linear-gradient(135deg,#b0a69a,#4a4038)"></div>
  <div class="ph" role="img" aria-label="Photo: woman wearing sunglasses" style="background:linear-gradient(135deg,#d8c8b8,#6a5040)"></div>
</div>

<!-- footer -->
<div class="abs foot-brand"><div class="mark"></div><div class="name">Tallbergsgillet</div></div>
<p class="abs foot-text">There are many variations of passages of Lorem Ipsum available, majority have suffered alteration in some form, by injected humour, or randomised words which don't look even stratum.</p>
<p class="abs sub-title">Email Subscription</p>
<div class="abs dark"></div>
<form class="abs sub-form">
  <span class="field">Enter Your Email...</span>
  <span class="go"><svg width="9" height="9" viewBox="0 0 9 9"><path d="M0.5 4.5L8.5 0.5 6 8.5 4.5 5z" fill="#fff"/></svg></span>
</form>
<div class="abs foot-social">
  <span><i></i></span><span class="on"><i></i></span><span><i></i></span><span><i></i></span><span><i></i></span><span><i></i></span>
</div>
<p class="abs copy">Copyright © 2016 Tallbergsgillet</p>

</body>
</html>
```